KWI Business Card

Please create a creative design for a business card using the new theme from the Logo & website. This company's main focus is food manufacturing building construction. Please integrate the new logo attached.

Please use the following information for the demo card:

Korvel Walls, Inc.
Dana Whitcombe
dwhitcombe@korvelwalls.example
Cell: 312-555-0178
218 Larkmoor Ave
Halvern Park, IN 60418

See pictures and more information on the website.

www.korvelwalls.example

```html
<!DOCTYPE html>
<html lang="en">
<head>
<meta charset="utf-8">
<title>KWI Business Card</title>
<link href="https://fonts.googleapis.com/css2?family=Montserrat:wght@700;800&family=Quicksand:wght@500;600&display=swap" rel="stylesheet">
<style>
  :root {
    --page: #e7e9ec;
    --blue: #1f6fc4;
    --blue-mid: #4d8ad6;
    --blue-light: #c9e2f6;
    --link-blue: #3f8ee0;
    --charcoal: #333333;
    --white: #ffffff;
  }
  * { margin: 0; padding: 0; box-sizing: border-box; }
  html, body { width: 1200px; height: 965px; overflow: hidden; background: var(--page); }
  .canvas { position: relative; width: 1200px; height: 965px; }
  .card {
    position: absolute; left: 300px; width: 600px; height: 343px;
    overflow: hidden; box-shadow: 0 6px 18px rgba(0,0,0,.18);
  }
  .card--front { top: 110px; }
  .card--back { top: 512px; background: var(--white); }

  .front-art {
    position: absolute; inset: 0;
    background: radial-gradient(ellipse 70% 80% at 55% 30%, var(--blue-light) 0%, #8fbde9 45%, var(--blue-mid) 100%);
  }
  .wordmark {
    font-family: "Montserrat", sans-serif; font-weight: 800;
    color: var(--blue); letter-spacing: .5px; white-space: nowrap;
  }
  .card--front .wordmark { position: absolute; left: 330px; top: 150px; font-size: 26px; }
  .card--back .wordmark { position: absolute; left: 34px; top: 74px; font-size: 26px; }

  .swoosh { position: absolute; inset: 0; }
  .holder-name {
    position: absolute; right: 30px; top: 28px;
    font-family: "Montserrat", sans-serif; font-weight: 700;
    font-size: 22px; color: var(--blue); text-transform: uppercase; letter-spacing: .3px;
  }
  .contact {
    position: absolute; right: 26px; top: 170px; list-style: none;
    font-family: "Quicksand", sans-serif; font-weight: 500; font-size: 15px;
    color: var(--white); text-align: right; line-height: 24px;
  }
  .contact li { display: flex; justify-content: flex-end; align-items: center; gap: 8px; white-space: nowrap; }
  .contact svg { width: 14px; height: 14px; flex: none; }
  .contact .accent { color: var(--link-blue); font-weight: 600; }
  .address {
    position: absolute; left: 34px; bottom: 24px; font-style: normal;
    font-family: "Quicksand", sans-serif; font-weight: 500; font-size: 16px;
    color: var(--blue-mid); line-height: 22px; white-space: nowrap;
  }
</style>
</head>
<body>
<main class="canvas">
  <section class="card card--front">
    <div class="front-art" role="img" aria-label="Soft blue gradient with a faint repeating snowflake pattern"></div>
    <div class="wordmark">Korvel Walls, Inc.</div>
  </section>

  <section class="card card--back">
    <svg class="swoosh" viewBox="0 0 600 343" preserveAspectRatio="none" aria-hidden="true">
      <defs>
        <linearGradient id="swooshBlue" x1="0" y1="0" x2="1" y2="0">
          <stop offset="0" stop-color="#1f6fc4"/>
          <stop offset="1" stop-color="#b9d6f3"/>
        </linearGradient>
      </defs>
      <path d="M0,205 Q330,175 600,62 Q330,198 0,236 Z" fill="url(#swooshBlue)"/>
      <path d="M0,256 Q330,215 600,78 L600,343 L0,343 Z" fill="var(--charcoal)"/>
    </svg>

    <div class="wordmark">Korvel Walls, Inc.</div>
    <h1 class="holder-name">Dana Whitcombe</h1>

    <ul class="contact">
      <li>312-555-0178
        <svg viewBox="0 0 14 14"><rect x="3.5" y="1" width="7" height="12" rx="1.5" fill="none" stroke="#3f8ee0" stroke-width="1.3"/><line x1="6" y1="11" x2="8" y2="11" stroke="#3f8ee0" stroke-width="1.2"/></svg>
      </li>
      <li>dwhitcombe@korvelwalls.example
        <svg viewBox="0 0 14 14"><rect x="1" y="3" width="12" height="8" fill="none" stroke="#3f8ee0" stroke-width="1.3"/><polyline points="1,3 7,8 13,3" fill="none" stroke="#3f8ee0" stroke-width="1.3"/></svg>
      </li>
      <li><span>www.<span class="accent">korvelwalls</span>.example</span>
        <svg viewBox="0 0 14 14"><circle cx="7" cy="7" r="6" fill="#3f8ee0"/><ellipse cx="7" cy="7" rx="2.5" ry="6" fill="none" stroke="#333" stroke-width=".9"/><line x1="1" y1="7" x2="13" y2="7" stroke="#333" stroke-width=".9"/></svg>
      </li>
    </ul>

    <address class="address">218 Larkmoor Ave<br>Halvern Park, IN 60418</address>
  </section>
</main>
</body>
</html>
```